Website for Brackley Fabrication & Construction Ltd

General Note to all.

1. Piling and gas works are separate areas of work and should not be put together.
- the marine section should really be the piling works and should have all the barges/water piles etc.
- the gas section should have the big silo looking thing

2. I would like to add in Specialist Onsite Labour and Management in the 'our services' section. The would include the Supervisors, Coded Welders, Site Fitters and Crane and Rig Crews etc.

3. I did like it how someone had use the BFC header logo as the top of the webpage with the individual tabs above and the website starting below. Please remove the VAT number and phone number from this section.

4. I also liked how one designer incorporate the orange line with spark (from the logo) as a page separator representing the welding part of the business

5. Add in a Mission Statement - To go above and beyond in to ensure our clients projects are delivered safely, ahead of schedule, in any environment for the benefit of not only our customers but also our employees and communities we work in.

6. Add in Business Objectives -BFC is on a mission to be one of the leading contractors in UK to supply All Site Labour - ranging from Site Management, fully Coded Welders, Site Fitters and Crane and Rig Crews.

7. I am happy for you to add in photos that are not ours for the thumbs nails for the our services. ie a colourful welding pics/cool tunnelling pic etc - just make sure I will not get done for copy write infringements

8. I would like a some type of 'contact us' field or 'request a consultation' section.

9. Please confirm if the webpages you create will be compatible for both desktop and mobile app and how difficult it will be to update personally once it is live.

10. You have all done very well and have thus far been very impressed with what you have produced. I gave a very vague brief as I was not entirely sure how you would go about making something with very little information. Some of the designs look very professional.

11. I'm not sure how once I choose the winning design how that then transfers over to my domain? Perhaps someone can help me with that? I will also be looking for a web hosting platform so feel free to provide this information.

After using Sketch hive for successful getting a professional logo for the company I'm giving the web design option a go.

I am looking for a professional website for the above civil construction company.

The company director has many years experience in Marine, tunnelling, conveyors, stadium construction gas and piling works including piling works for coal ports, bridges and tunnels.

The company currently provide 20+ skilled and experienced guys from all trades (supervisors, coded welders, fitters, crane drivers and crane supervisors, rigglers, slingers and piling operatives) on the Corran Flowpath project in London - London's new super sewer. Most of this work is off barges carrying cranes (upto 600T and drill rigs).

As we are looking to expand and get more subcontracts we need a web presence to say who we are and what we do.

I'll include the 2 company logos we currently use below

I have included an info doc with pics you may or may not use.

Target Market(s)

Mainly other large construction companies and potential subcontractors

Industry/Entity Type

Construction Company

Coding

Coded - Design and coding required

Font styles to use
Sans Serif

Colors
0655a3
f37122
ffffff

Requirements
Must have
• Few tabs
• Simple to use/update but still professional look
• The challenge will be making the website look professional with not much available content.
Should not have
• No residential house building

```html
<!DOCTYPE html>
<html lang="en">
<head>
<meta charset="utf-8">
<title>What we Offer</title>
<link href="https://fonts.googleapis.com/css2?family=Poppins:wght@300;400;800&family=Montserrat:wght@400&family=Roboto:wght@400;700&display=swap" rel="stylesheet">
<style>
  :root {
    --navy: #0d3a7c;
    --ink: #111111;
    --muted: #9a9a9a;
    --orange: #f37122;
    --blue: #0655a3;
    --white: #ffffff;
    --band-start: #d5834c;
    --band-mid: #b0708c;
    --band-end: #7a5bd8;
    --icon-grad: linear-gradient(45deg, #0d3a7c 0%, #f37122 100%);
  }
  * { box-sizing: border-box; margin: 0; padding: 0; }
  html, body { width: 1200px; height: 1000px; overflow: hidden; background: var(--white); }
  .page { position: relative; width: 1200px; height: 1000px; }

  .offer-title {
    position: absolute; top: 4px; left: 0; width: 1200px; text-align: center;
    font: 800 33px/46px "Poppins", sans-serif; color: var(--navy);
  }
  .offer-intro {
    position: absolute; top: 61px; left: 260px; width: 680px; text-align: center;
    font: 300 15px/22px "Poppins", sans-serif; color: var(--ink);
  }

  .service { position: absolute; width: 260px; }
  .service-icon {
    position: absolute; left: 0; top: 2px; width: 34px; height: 34px;
    border-radius: 8px; background: var(--icon-grad);
  }
  .service-name {
    position: absolute; top: -2px; font: 400 15px/20px "Poppins", sans-serif; color: var(--ink);
  }
  .service-text {
    position: absolute; top: 26px; width: 165px;
    font: 400 11.5px/18px "Montserrat", sans-serif; color: var(--muted);
  }

  .achievement {
    position: absolute; top: 507px; left: 0; width: 1200px; height: 333px;
    background: linear-gradient(90deg, var(--band-start) 0%, var(--band-mid) 55%, var(--band-end) 100%);
    color: var(--white); font-family: "Roboto", sans-serif;
  }
  .achievement-kicker { position: absolute; left: 333px; top: 84px; font-size: 9px; letter-spacing: 1px; }
  .achievement-title { position: absolute; left: 333px; top: 101px; font-size: 26px; line-height: 32px; font-weight: 400; }
  .stat { position: absolute; top: 192px; }
  .stat-value { font-size: 36px; font-weight: 700; line-height: 40px; }
  .stat-label { font-size: 9px; font-weight: 700; margin-left: 2px; margin-top: 6px; }
  .play-button { position: absolute; left: 789px; top: 138px; }

  .gallery { position: absolute; top: 840px; left: 0; width: 1200px; height: 160px; display: flex; }
  .gallery-tile { height: 160px; }
</style>
</head>
<body>
<main class="page">
  <h1 class="offer-title">What we Offer</h1>
  <p class="offer-intro">Lorem ipsum dolor sit amet conse ctetur adipisicing elit, sed do eiusmod tempor incidi-dunt ut labore et dolore magna aliqua. Ut enim ad minim veniam, quis nostrud.</p>

  <section class="service" style="left:208px; top:165px;">
    <div class="service-icon" role="img" aria-label="Ducting icon"></div>
    <h2 class="service-name" style="left:63px;">Ducting</h2>
    <p class="service-text" style="left:67px;">Lorem ipsum dolor sit amet conse ctetur adipisicing elit, sed do eiusmod tempor incididunt ut labore et dolore magna aliqua.</p>
  </section>

  <section class="service" style="left:491px; top:165px;">
    <div class="service-icon" role="img" aria-label="Stacks icon"></div>
    <h2 class="service-name" style="left:65px;">Stacks</h2>
    <p class="service-text" style="left:68px;">Lorem ipsum dolor sit amet conse ctetur adipisicing elit, sed do eiusmod tempor incididunt ut labore et dolore magna aliqua.</p>
  </section>

  <section class="service" style="left:773px; top:165px;">
    <div class="service-icon" role="img" aria-label="Structural icon"></div>
    <h2 class="service-name" style="left:55px;">Structural</h2>
    <p class="service-text" style="left:54px;">Lorem ipsum dolor sit amet conse ctetur adipisicing elit, sed do eiusmod tempor incididunt ut labore et dolore magna aliqua.</p>
  </section>

  <section class="service" style="left:208px; top:346px;">
    <div class="service-icon" role="img" aria-label="Tanks icon"></div>
    <h2 class="service-name" style="left:63px;">Tanks</h2>
    <p class="service-text" style="left:67px;">Lorem ipsum dolor sit amet conse ctetur adipisicing elit, sed do eiusmod tempor incididunt ut labore et dolore magna aliqua.</p>
  </section>

  <section class="service" style="left:491px; top:346px;">
    <div class="service-icon" role="img" aria-label="Conveyer system icon"></div>
    <h2 class="service-name" style="left:65px;">Conveyer system</h2>
    <p class="service-text" style="left:68px;">Lorem ipsum dolor sit amet conse ctetur adipisicing elit, sed do eiusmod tempor incididunt ut labore et dolore magna aliqua.</p>
  </section>

  <section class="service" style="left:773px; top:346px;">
    <div class="service-icon" role="img" aria-label="Architectural icon"></div>
    <h2 class="service-name" style="left:55px;">Architectural</h2>
    <p class="service-text" style="left:54px;">Lorem ipsum dolor sit amet conse ctetur adipisicing elit, sed do eiusmod tempor incididunt ut labore et dolore magna aliqua.</p>
  </section>

  <section class="achievement" role="img" aria-label="Photo of tall lattice crane booms against the sky, under an orange-to-purple tint">
    <p class="achievement-kicker">OUR'S ACHIEVEMENT</p>
    <h2 class="achievement-title">4578+ Project Complited<br>Hole Over the world.</h2>
    <div class="stat" style="left:333px;"><div class="stat-value">2315</div><div class="stat-label">Clients</div></div>
    <div class="stat" style="left:457px;"><div class="stat-value">3043</div><div class="stat-label">Memberes</div></div>
    <div class="stat" style="left:587px;"><div class="stat-value">125</div><div class="stat-label">Awards</div></div>
    <svg class="play-button" width="58" height="58" viewBox="0 0 58 58" fill="none" stroke="#fff" stroke-width="2">
      <circle cx="29" cy="29" r="27"/><path d="M22 17 L40 29 L22 41 Z" stroke-linejoin="round"/>
    </svg>
  </section>

  <div class="gallery">
    <div class="gallery-tile" style="width:296px; background:linear-gradient(180deg,#3b78d6 0%,#5a8fd8 45%,#e6e0d4 100%);" role="img" aria-label="Photo of a steel structure with railings under a blue sky"></div>
    <div class="gallery-tile" style="width:302px; background:linear-gradient(135deg,#6a5a4a 0%,#a83a4a 45%,#c94d8e 100%);" role="img" aria-label="Photo of a welder at work with bright sparks"></div>
    <div class="gallery-tile" style="width:302px; background:linear-gradient(180deg,#9cc2ec 0%,#b8d0ea 55%,#7d7a52 100%);" role="img" aria-label="Photo of barges carrying piling rigs and cranes on the river"></div>
    <div class="gallery-tile" style="width:300px; background:linear-gradient(180deg,#e4e6e4 0%,#c9cbc6 55%,#8f918c 100%);" role="img" aria-label="Photo of a large gas storage tank under construction in fog"></div>
  </div>
</main>
</body>
</html>
```